Business card design for Medical Practice Mgmt company
Ashfield Clinic Allies
Business card design for Medical Practice Mgmt company - Medical
Creative Brief
Professional
Monica Daltrey
VP of Operations
4170 E Holloway Ln # 210 Plano, TX 75041
mdaltrey@aca-mail.net
www.ashfieldclinicallies.net
jdovan jdovan
uploaded AI file
bluefern bluefern
Logo Ai file needed!

```html
<!DOCTYPE html>
<html lang="en">
<head>
<meta charset="utf-8">
<title>Ashfield Clinic Allies – Business Card</title>
<link href="https://fonts.googleapis.com/css2?family=Montserrat:wght@400;500;600;700&display=swap" rel="stylesheet">
<style>
  :root {
    --stage: #e4e4e4;
    --card-white: #ffffff;
    --card-black: #0c0c0c;
    --brand-navy: #1c2a44;
    --brand-blue: #2f7fc1;
    --rule-grey: #9a9a9a;
    --text-grey: #4a4a4a;
    --text-light: #d8d8d8;
  }
  * { margin: 0; padding: 0; box-sizing: border-box; }
  html, body {
    width: 1200px; height: 984px; overflow: hidden;
    background: var(--stage);
    font-family: "Montserrat", sans-serif;
  }
  .canvas { position: relative; width: 1200px; height: 984px; }

  .card {
    position: absolute; left: 250px; width: 700px; height: 400px;
    border-radius: 22px; overflow: hidden;
    box-shadow: 0 6px 18px rgba(0,0,0,0.18);
  }

  /* Back side */
  .card-back { top: 56px; background: var(--card-black); }
  .back-brand {
    position: absolute; top: 150px; left: 0; width: 100%;
    display: flex; align-items: center; justify-content: center; gap: 14px;
  }
  .back-brand-dot { width: 34px; height: 34px; border-radius: 50%; background: var(--brand-blue); }
  .back-brand-name { color: #ffffff; font-weight: 600; font-size: 26px; letter-spacing: 1px; }
  .back-web {
    position: absolute; left: 40px; bottom: 36px;
    color: var(--text-light); font-size: 15px; letter-spacing: 3px;
  }

  /* Front side */
  .card-front { top: 528px; background: var(--card-white); }
  .front-wave { position: absolute; inset: 0; }
  .front-brand { position: absolute; left: 38px; top: 100px; }
  .front-brand-name {
    color: var(--brand-navy); font-weight: 600; font-size: 30px; letter-spacing: 0.5px;
  }
  .front-tagline {
    margin-top: 6px; color: var(--text-grey); font-size: 9px;
    letter-spacing: 1.5px; text-transform: uppercase;
  }
  .person { position: absolute; left: 38px; top: 200px; }
  .person-name { color: var(--brand-blue); font-weight: 600; font-size: 22px; }
  .person-title { margin-top: 4px; color: var(--text-grey); font-size: 15px; }

  .contact-list {
    position: absolute; left: 420px; top: 226px; list-style: none;
    color: var(--text-grey); font-size: 11px; line-height: 1.45;
  }
  .contact-list li { display: flex; align-items: flex-start; gap: 8px; }
  .contact-icon { flex: 0 0 auto; margin-top: 2px; }
</style>
</head>
<body>
<main class="canvas">

  <section class="card card-back" aria-label="Card back">
    <div class="back-brand">
      <span class="back-brand-dot"></span>
      <span class="back-brand-name">Ashfield Clinic Allies</span>
    </div>
    <p class="back-web">www.ashfieldclinicallies.net</p>
  </section>

  <section class="card card-front" aria-label="Card front">
    <svg class="front-wave" width="700" height="400" viewBox="0 0 700 400">
      <path d="M395 0 H700 V270 C640 190 520 160 470 90 C445 55 420 20 395 0 Z" fill="var(--card-black)"/>
      <path d="M0 80 C150 50 300 30 400 12" fill="none" stroke="var(--brand-blue)" stroke-width="4"/>
      <path d="M0 180 C150 165 280 162 360 168" fill="none" stroke="var(--rule-grey)" stroke-width="1.5"/>
    </svg>

    <div class="front-brand">
      <p class="front-brand-name">Ashfield Clinic Allies</p>
      <p class="front-tagline">Empowering Practices, Improving Patient Outcomes</p>
    </div>

    <div class="person">
      <p class="person-name">Monica Daltrey</p>
      <p class="person-title">VP of Operations</p>
    </div>

    <ul class="contact-list">
      <li>
        <svg class="contact-icon" width="10" height="10" viewBox="0 0 10 10"><circle cx="5" cy="5" r="5" fill="var(--brand-blue)"/><circle cx="5" cy="4" r="1.6" fill="#fff"/></svg>
        <span>4170 E Holloway Ln # 210<br>Plano, TX 75041</span>
      </li>
      <li>
        <svg class="contact-icon" width="10" height="10" viewBox="0 0 10 10"><circle cx="5" cy="5" r="5" fill="var(--brand-blue)"/><rect x="3.5" y="2.5" width="3" height="5" rx="0.6" fill="#fff"/></svg>
        <span>469-555-0142</span>
      </li>
      <li>
        <svg class="contact-icon" width="10" height="10" viewBox="0 0 10 10"><circle cx="5" cy="5" r="5" fill="var(--brand-blue)"/><rect x="3.5" y="2.5" width="3" height="5" rx="0.6" fill="#fff"/></svg>
        <span>469-555-0178</span>
      </li>
      <li>
        <svg class="contact-icon" width="10" height="10" viewBox="0 0 10 10"><circle cx="5" cy="5" r="5" fill="var(--brand-blue)"/><rect x="3" y="3" width="4" height="4" fill="#fff"/></svg>
        <span>469-555-0193</span>
      </li>
      <li>
        <svg class="contact-icon" width="10" height="10" viewBox="0 0 10 10"><circle cx="5" cy="5" r="5" fill="var(--brand-blue)"/><rect x="2.5" y="3.2" width="5" height="3.6" fill="#fff"/></svg>
        <span>mdaltrey@aca-mail.net</span>
      </li>
      <li>
        <svg class="contact-icon" width="10" height="10" viewBox="0 0 10 10"><circle cx="5" cy="5" r="5" fill="var(--brand-blue)"/><circle cx="5" cy="5" r="2.4" fill="none" stroke="#fff" stroke-width="1"/></svg>
        <span>www.ashfieldclinicallies.net</span>
      </li>
    </ul>
  </section>

</main>
</body>
</html>
```